Corporate Trainning business needs PPT template for sales, reports and projects

Create a power point template with own design and rich in distinctness of our brand, logo and industry (corporate training). Enough slides templates to use for sales, reports and projects development: flowcharts, roadmaps, bullets, service categories, description box, title & subtitle slides, bar & pie charts, calendars, gantt, some basic shapes and icons (training, education, elearning, etc related).
Enclose: color palette, set of logo for different uses and ppt presentation with some ideas and slide templates. The ppt hope could help, but I trust in your experience and creativity.

Target Market(s)

Company training

Industry/Entity Type

Training - Education

Font styles to use
Sans Serif

Requirements
Nice to have
• Relative to training icons

```html
<!DOCTYPE html>
<html lang="en">
<head>
<meta charset="utf-8">
<title>Veltora – Presentation Template</title>
<link href="https://fonts.googleapis.com/css2?family=Montserrat:wght@500;600;700;800&family=Roboto:wght@400;500;700&display=swap" rel="stylesheet">
<style>
  :root{
    --canvas:#e4e6ea;
    --navy:#0f1f3d;
    --navy-deep:#0a1730;
    --gold:#e3b920;
    --teal:#1f7a93;
    --teal-light:#5bc0d0;
    --grey-bar:#b3b3b3;
    --text:#222;
    --muted:#8a8a8a;
    --white:#fff;
  }
  *{margin:0;padding:0;box-sizing:border-box}
  html,body{width:1200px;height:4051px;overflow:hidden}
  body{background:var(--canvas);font-family:'Roboto',Arial,sans-serif;color:var(--text);position:relative}
  .slide{position:absolute;left:77px;width:1047px;height:588px;background:var(--white);overflow:hidden;box-shadow:0 2px 6px rgba(0,0,0,.06)}
  .abs{position:absolute}
  .head-marker{position:absolute;left:0;top:34px;width:0;height:0;border-top:21px solid transparent;border-bottom:21px solid transparent;border-left:39px solid var(--gold)}
  .head-title{position:absolute;left:60px;top:40px;font-family:'Montserrat',sans-serif;font-weight:700;font-size:24px;color:var(--teal);letter-spacing:.3px}
  .brand{position:absolute;left:763px;top:28px;display:flex;align-items:center;gap:12px}
  .brand-dot{width:40px;height:40px;border-radius:50%;background:var(--gold)}
  .brand-name{font-family:'Montserrat',sans-serif;font-weight:500;font-size:44px;color:var(--navy);line-height:1}
  .brand.light .brand-name{color:var(--white)}

  /* Title slide */
  .title-slide{top:88px;background:linear-gradient(120deg,#12264a 0%,#0c1c38 55%,#08152b 100%)}
  .title-rule-v{left:118px;top:210px;width:3px;height:167px;background:var(--gold)}
  .title-rule-h{left:0;top:291px;width:118px;height:3px;background:var(--gold)}
  .title-text{left:141px;top:196px;font-family:'Montserrat',sans-serif;font-weight:800;font-size:46px;line-height:67px;color:var(--white);letter-spacing:.5px}
  .hero-visual{left:565px;top:146px;width:332px;height:366px;border-radius:50% 50% 50% 50%/45% 45% 55% 55%;background:radial-gradient(circle at 60% 40%,#6b5448 0%,#2a3550 55%,#0f1f3d 100%)}

  /* Solutions */
  .sol-slide{top:738px}
  .sol-item{position:absolute;width:290px;text-align:center}
  .icon-bubble{width:84px;height:84px;border-radius:50%;background:var(--white);box-shadow:0 4px 10px rgba(0,0,0,.15);margin:0 auto;display:flex;align-items:center;justify-content:center}
  .sol-item h3{margin-top:18px;font-size:14px;font-weight:700;color:var(--text)}
  .sol-item p{margin-top:12px;font-size:11.5px;line-height:19px;color:var(--muted)}

  /* Values */
  .val-slide{top:1397px}
  .portrait-ring{left:86px;top:132px;width:407px;height:407px;border-radius:50%;background:var(--gold)}
  .portrait{left:94px;top:132px;width:403px;height:407px;border-radius:50%;background:linear-gradient(135deg,#d8d2c8 0%,#9aa6b5 45%,#4d6690 100%)}
  .val-badge{width:82px;height:82px;border-radius:50%;border:5px solid var(--white);box-shadow:0 3px 10px rgba(0,0,0,.25);display:flex;align-items:center;justify-content:center}
  .val-item h3{font-size:20px;font-weight:700;color:var(--navy)}
  .val-item p{margin-top:8px;font-size:14px;line-height:21px;color:var(--muted);width:330px}

  /* Features */
  .feat-slide{top:2056px}
  .feat-tile{width:75px;height:70px;display:flex;align-items:center;justify-content:center}
  .feat-text h3{font-size:17px;font-weight:700;color:var(--text)}
  .feat-text p{margin-top:10px;font-size:12.5px;line-height:20px;color:var(--muted);width:180px}
  .feat-text.right{text-align:right}
  .feat-text.right p{margin-left:auto}
  .center-mark{left:388px;top:197px;width:268px;height:268px;border-radius:50%;background:var(--gold);display:flex;align-items:center;justify-content:center}
  .center-mark span{font-family:'Montserrat',sans-serif;font-weight:500;font-size:38px;color:var(--navy)}

  /* Benefits */
  .ben-slide{top:2715px}
  .ben-card{position:absolute;top:164px;width:305px;height:338px;background:var(--white);border-radius:16px;box-shadow:0 4px 14px rgba(0,0,0,.12);text-align:center;padding-top:35px}
  .ben-icon{width:88px;height:88px;border-radius:50%;margin:0 auto;display:flex;align-items:center;justify-content:center}
  .ben-card h3{margin-top:30px;font-size:14px;font-weight:700;line-height:20px;color:var(--text)}
  .ben-card p{margin:14px auto 0;width:275px;font-size:12px;line-height:21.5px;color:var(--muted)}

  /* Chart */
  .chart-slide{top:3374px}
  .chart{left:0;top:0}
  .bullets{left:698px;top:155px;width:300px;list-style:none}
  .bullets li{position:absolute;left:0;width:300px;padding-left:20px;font-size:12px;line-height:20px;color:var(--muted)}
  .bullets li::before{content:"";position:absolute;left:0;top:5px;width:11px;height:11px;border-radius:50%;background:var(--gold)}
  .bullets li::after{content:"";position:absolute;left:3px;top:7px;width:4px;height:6px;border:solid var(--white);border-width:0 1.5px 1.5px 0;transform:rotate(45deg)}
</style>
</head>
<body>

<!-- Title slide -->
<section class="slide title-slide">
  <div class="brand light"><div class="brand-dot"></div><div class="brand-name">Veltora</div></div>
  <div class="abs title-rule-h"></div>
  <div class="abs title-rule-v"></div>
  <h1 class="abs title-text">WELCOME<br>TO THE<br>VELTORA</h1>
  <div class="abs hero-visual" role="img" aria-label="Photo of a person working at a desk with a laptop, set in a rounded frame"></div>
</section>

<!-- Solutions -->
<section class="slide sol-slide">
  <div class="head-marker"></div>
  <h2 class="head-title">VELTORA SOLUTIONS</h2>
  <div class="brand"><div class="brand-dot"></div><div class="brand-name">Veltora</div></div>

  <div class="sol-item" style="left:55px;top:122px">
    <div class="icon-bubble"><svg width="40" height="40" viewBox="0 0 40 40" fill="none" stroke="#1f7a93" stroke-width="2"><circle cx="20" cy="16" r="11"/><circle cx="20" cy="16" r="6"/><path d="M13 25l-4 11 6-3 3 5 2-10M27 25l4 11-6-3-3 5-2-10"/></svg></div>
    <h3>BRAND ID</h3>
    <p>Lorem ipsum dolor sit amet, consectetur adipisc ing elit, sed do eiusmod tempor incididunt ut labore et dolore magna aliqua.</p>
  </div>
  <div class="sol-item" style="left:377px;top:122px">
    <div class="icon-bubble"><svg width="40" height="40" viewBox="0 0 40 40" fill="none" stroke="#1f7a93" stroke-width="2"><path d="M4 22l10-10 6 4 6-4 10 10-10 8-6-4-6 4z"/><path d="M20 4v5M11 6l2 4M29 6l-2 4"/></svg></div>
    <h3>STARTUP SUPPORT</h3>
    <p>Lorem ipsum dolor sit amet, consectetur adipisc ing elit, sed do eiusmod tempor incididunt ut labore et dolore magna aliqua.</p>
  </div>
  <div class="sol-item" style="left:700px;top:122px">
    <div class="icon-bubble"><svg width="40" height="40" viewBox="0 0 40 40" fill="none" stroke="#1f7a93" stroke-width="2"><circle cx="16" cy="20" r="11"/><path d="M5 20v-3a11 11 0 0 1 22 0v3"/><rect x="24" y="5" width="12" height="9" rx="2"/><path d="M16 31h6"/></svg></div>
    <h3>CALL CENTER</h3>
    <p>Lorem ipsum dolor sit amet, consectetur adipisc ing elit, sed do eiusmod tempor incididunt ut labore et dolore magna aliqua.</p>
  </div>
  <div class="sol-item" style="left:55px;top:354px">
    <div class="icon-bubble"><svg width="40" height="40" viewBox="0 0 40 40" fill="none" stroke="#1f7a93" stroke-width="2"><rect x="4" y="6" width="26" height="20" rx="2"/><circle cx="26" cy="26" r="7"/><path d="M31 31l6 6M9 20l5-5 4 3 6-6"/></svg></div>
    <h3>MARKET RESEARCH</h3>
    <p>Lorem ipsum dolor sit amet, consectetur adipisc ing elit, sed do eiusmod tempor incididunt ut labore et dolore magna aliqua.</p>
  </div>
  <div class="sol-item" style="left:377px;top:354px">
    <div class="icon-bubble"><svg width="40" height="40" viewBox="0 0 40 40" fill="none" stroke="#1f7a93" stroke-width="2"><path d="M20 4l12 5v9c0 8-6 13-12 16-6-3-12-8-12-16V9z"/><rect x="14" y="17" width="12" height="9"/><path d="M16 17v-3a4 4 0 0 1 8 0v3"/></svg></div>
    <h3>SECURITY CONTROL</h3>
    <p>Lorem ipsum dolor sit amet, consectetur adipisc ing elit, sed do eiusmod tempor incididunt ut labore et dolore magna aliqua.</p>
  </div>
  <div class="sol-item" style="left:700px;top:354px">
    <div class="icon-bubble"><svg width="40" height="40" viewBox="0 0 40 40" fill="none" stroke="#1f7a93" stroke-width="2"><circle cx="10" cy="10" r="5"/><rect x="24" y="5" width="11" height="9" rx="2"/><circle cx="20" cy="22" r="5"/><rect x="5" y="28" width="10" height="8" rx="2"/><circle cx="31" cy="31" r="5"/><path d="M14 13l3 5M24 14l-2 4M16 26l-3 2M24 25l4 3"/></svg></div>
    <h3>SOCIAL MEDIA</h3>
    <p>Lorem ipsum dolor sit amet, consectetur adipisc ing elit, sed do eiusmod tempor incididunt ut labore et dolore magna aliqua.</p>
  </div>
</section>

<!-- Values -->
<section class="slide val-slide">
  <div class="head-marker"></div>
  <h2 class="head-title">VELTORA VALUES</h2>
  <div class="brand"><div class="brand-dot"></div><div class="brand-name">Veltora</div></div>

  <div class="abs portrait-ring"></div>
  <div class="abs portrait" role="img" aria-label="Photo of a smiling man with headphones writing notes at a desk"></div>

  <svg class="abs" style="left:520px;top:140px" width="120" height="390" viewBox="0 0 120 390" fill="none">
    <path d="M8 8 C70 60 90 110 95 195 C90 280 70 330 8 382" stroke="#555" stroke-width="1.5" stroke-dasharray="2 4"/>
    <circle cx="8" cy="8" r="3.5" fill="#333"/><circle cx="8" cy="382" r="3.5" fill="#333"/>
  </svg>

  <div class="abs val-badge" style="left:535px;top:182px;background:var(--navy)"><svg width="36" height="36" viewBox="0 0 36 36" fill="none" stroke="#fff" stroke-width="1.8"><path d="M4 20l8-8 6 4 6-4 8 8-8 7-6-4-6 4z"/><circle cx="18" cy="8" r="3"/></svg></div>
  <div class="abs val-badge" style="left:566px;top:297px;background:var(--teal)"><svg width="36" height="36" viewBox="0 0 36 36" fill="none" stroke="#fff" stroke-width="1.8"><circle cx="18" cy="18" r="14"/><circle cx="18" cy="18" r="8"/><circle cx="18" cy="18" r="3"/></svg></div>
  <div class="abs val-badge" style="left:536px;top:412px;background:var(--navy)"><svg width="36" height="36" viewBox="0 0 36 36" fill="none" stroke="#fff" stroke-width="1.8"><rect x="6" y="4" width="20" height="28" rx="2"/><circle cx="16" cy="13" r="4"/><path d="M10 22h12M10 26h8M28 18l4 4-8 8h-4v-4z"/></svg></div>

  <div class="abs val-item" style="left:632px;top:186px"><h3>We love innovations</h3><p>lorem ipsum dolor sit amet, consectetuer adip iscing elit. maecenas porttitor</p></div>
  <div class="abs val-item" style="left:662px;top:301px"><h3>We respect the nature</h3><p>lorem ipsum dolor sit amet, consectetuer adip iscing elit. maecenas porttitor</p></div>
  <div class="abs val-item" style="left:634px;top:416px"><h3>We believe in future</h3><p>lorem ipsum dolor sit amet, consectetuer adip iscing elit. maecenas porttitor</p></div>
</section>

<!-- Features -->
<section class="slide feat-slide">
  <div class="head-marker"></div>
  <h2 class="head-title">OUR FEATURES</h2>
  <div class="brand"><div class="brand-dot"></div><div class="brand-name">Veltora</div></div>

  <div class="abs center-mark"><span>Veltora</span></div>

  <div class="abs feat-tile" style="left:46px;top:190px;background:var(--teal)"><svg width="40" height="40" viewBox="0 0 40 40" fill="none" stroke="#fff" stroke-width="2"><circle cx="20" cy="16" r="11"/><circle cx="20" cy="16" r="6"/><path d="M13 25l-4 11 6-3 3 5 2-10M27 25l4 11-6-3-3 5-2-10"/></svg></div>
  <div class="abs feat-text" style="left:146px;top:188px"><h3>FEATURE ONE</h3><p>Lorem ipsum dolor sit amet consectetur adipiscing elit sed do eiusmod</p></div>

  <div class="abs feat-tile" style="left:46px;top:390px;background:var(--gold)"><svg width="40" height="40" viewBox="0 0 40 40" fill="none" stroke="#fff" stroke-width="2"><path d="M20 34S4 24 4 14a8 8 0 0 1 16-2 8 8 0 0 1 16 2c0 10-16 20-16 20z"/><path d="M12 20l5-4 4 3 5-3"/></svg></div>
  <div class="abs feat-text" style="left:146px;top:388px"><h3>FEATURE TWO</h3><p>Lorem ipsum dolor sit amet consectetur adipiscing elit sed do eiusmod</p></div>

  <div class="abs feat-tile" style="left:925px;top:190px;background:var(--navy)"><svg width="40" height="40" viewBox="0 0 40 40" fill="none" stroke="#fff" stroke-width="2"><circle cx="20" cy="9" r="5"/><path d="M12 26v-6a8 8 0 0 1 16 0v6"/><path d="M8 30l2 4 2-4M18 30l2 4 2-4M28 30l2 4 2-4"/></svg></div>
  <div class="abs feat-text right" style="left:718px;top:188px;width:180px"><h3>FEATURE THREE</h3><p>Lorem ipsum dolor sit amet consectetur adipiscing elit sed do eiusmod</p></div>

  <div class="abs feat-tile" style="left:925px;top:390px;background:var(--teal-light)"><svg width="40" height="40" viewBox="0 0 40 40" fill="none" stroke="#fff" stroke-width="2"><path d="M14 30v-4a10 10 0 1 1 12 0v4z"/><path d="M16 34h8"/><circle cx="20" cy="17" r="4"/></svg></div>
  <div class="abs feat-text right" style="left:718px;top:388px;width:180px"><h3>FEATURE FOUR</h3><p>Lorem ipsum dolor sit amet consectetur adipiscing elit sed do eiusmod</p></div>
</section>

<!-- Benefits -->
<section class="slide ben-slide">
  <div class="head-marker"></div>
  <h2 class="head-title">BENEFITS</h2>
  <div class="brand"><div class="brand-dot"></div><div class="brand-name">Veltora</div></div>

  <article class="ben-card" style="left:41px">
    <div class="ben-icon" style="background:var(--gold)"><svg width="44" height="44" viewBox="0 0 44 44" fill="none" stroke="#fff" stroke-width="2"><circle cx="22" cy="22" r="8"/><circle cx="22" cy="22" r="3"/><path d="M22 6v6M22 32v6M6 22h6M32 22h6M11 11l4 4M29 29l4 4M33 11l-4 4M11 33l4-4"/></svg></div>
    <h3>WE PROVIDE<br>360-DEGREE SOLUTION</h3>
    <p>Sed ut perspiciatis unde omnis iste natus error sit voluptatem accusantium doloremque lau dantium, totam rem aperiam, eaque ipsa quae ab illo inventore veritatis et quasi architecto beatae vitae sunt explicabo.</p>
  </article>
  <article class="ben-card" style="left:371px">
    <div class="ben-icon" style="background:var(--teal)"><svg width="44" height="44" viewBox="0 0 44 44" fill="none" stroke="#fff" stroke-width="2"><rect x="8" y="6" width="28" height="32" rx="2"/><path d="M13 13h18M13 19h18M13 25h10M13 31h6"/></svg></div>
    <h3>SAVE UP TO $500<br>WITH SUBSCRIPTION</h3>
    <p>Sed ut perspiciatis unde omnis iste natus error sit voluptatem accusantium doloremque lau dantium, totam rem aperiam, eaque ipsa quae ab illo inventore veritatis et quasi architecto beatae vitae sunt explicabo.</p>
  </article>
  <article class="ben-card" style="left:700px">
    <div class="ben-icon" style="background:var(--navy)"><svg width="44" height="44" viewBox="0 0 44 44" fill="none" stroke="#fff" stroke-width="2"><circle cx="22" cy="16" r="9"/><circle cx="22" cy="16" r="3"/><path d="M6 34l8-6h10l4 3h6M6 38h30"/></svg></div>
    <h3>WE PROVIDE<br>24/7 SUPPORT</h3>
    <p>Sed ut perspiciatis unde omnis iste natus error sit voluptatem accusantium doloremque lau dantium, totam rem aperiam, eaque ipsa quae ab illo inventore veritatis et quasi architecto beatae vitae sunt explicabo.</p>
  </article>
</section>

<!-- Chart -->
<section class="slide chart-slide">
  <div class="head-marker"></div>
  <h2 class="head-title">SMART CHART - ANNUAL SALES, K-USD</h2>
  <div class="brand"><div class="brand-dot"></div><div class="brand-name">Veltora</div></div>

  <svg class="abs chart" width="680" height="588" viewBox="0 0 680 588" font-family="Roboto, Arial, sans-serif" font-size="11" font-weight="700" fill="#222">
    <g stroke="#e2e2e2" stroke-width="1">
      <line x1="85" y1="151" x2="643" y2="151"/><line x1="85" y1="208" x2="643" y2="208"/>
      <line x1="85" y1="266" x2="643" y2="266"/><line x1="85" y1="323" x2="643" y2="323"/>
      <line x1="85" y1="380" x2="643" y2="380"/><line x1="85" y1="438" x2="643" y2="438"/>
      <line x1="85" y1="495" x2="643" y2="495"/>
      <line x1="85" y1="151" x2="85" y2="495"/><line x1="165" y1="151" x2="165" y2="495"/>
      <line x1="244" y1="151" x2="244" y2="495"/><line x1="324" y1="151" x2="324" y2="495"/>
      <line x1="404" y1="151" x2="404" y2="495"/><line x1="484" y1="151" x2="484" y2="495"/>
      <line x1="563" y1="151" x2="563" y2="495"/><line x1="643" y1="151" x2="643" y2="495"/>
    </g>
    <g text-anchor="end">
      <text x="72" y="155">120</text><text x="72" y="212">100</text><text x="72" y="270">80</text>
      <text x="72" y="327">60</text><text x="72" y="384">40</text><text x="72" y="442">20</text><text x="72" y="499">0</text>
    </g>
    <!-- bars: 0 at y=495, 1 unit = 2.867px -->
    <g fill="#0f1f3d">
      <rect x="106" y="208" width="16" height="287"/><rect x="186" y="237" width="16" height="258"/>
      <rect x="265" y="352" width="16" height="143"/><rect x="345" y="208" width="16" height="287"/>
      <rect x="425" y="208" width="16" height="287"/><rect x="505" y="323" width="16" height="172"/>
      <rect x="584" y="352" width="16" height="143"/>
    </g>
    <g fill="#b3b3b3">
      <rect x="130" y="237" width="16" height="258"/><rect x="210" y="266" width="16" height="229"/>
      <rect x="289" y="208" width="16" height="287"/><rect x="369" y="323" width="16" height="172"/>
      <rect x="449" y="237" width="16" height="258"/><rect x="529" y="280" width="16" height="215"/>
      <rect x="608" y="208" width="16" height="287"/>
    </g>
    <g text-anchor="middle" font-size="10.5">
      <text x="114" y="202">100</text><text x="138" y="231">90</text>
      <text x="194" y="231">90</text><text x="218" y="260">80</text>
      <text x="273" y="346">50</text><text x="297" y="202">100</text>
      <text x="353" y="202">100</text><text x="377" y="317">60</text>
      <text x="433" y="202">100</text><text x="457" y="231">90</text>
      <text x="513" y="317">60</text><text x="537" y="274">75</text>
      <text x="592" y="346">50</text><text x="616" y="202">100</text>
    </g>
    <g text-anchor="middle" font-size="11.5">
      <text x="125" y="519">Sun</text><text x="205" y="519">Mon</text><text x="284" y="519">Tue</text>
      <text x="364" y="519">Wed</text><text x="444" y="519">Thu</text><text x="524" y="519">Fri</text><text x="603" y="519">Sat</text>
    </g>
  </svg>

  <ul class="abs bullets">
    <li style="top:0">Lorem ipsum dolor sit consectetur adipiscing elit, sed do eiusmod tempor incididunt ut labore et dolore magna aliqua.</li>
    <li style="top:71px">Lorem ipsum dolor sit consectetur adipiscing elit, sed do eiusmod</li>
    <li style="top:124px">Lorem ipsum dolor sit consectetur adipiscing elit, sed do eiusmod tempor incididunt ut labore et dolore magna aliqua.</li>
    <li style="top:195px">Lorem ipsum dolor sit consectetur adipiscing elit, sed do eiusmod</li>
    <li style="top:248px">Lorem ipsum dolor sit consectetur adipiscing elit, sed do eiusmod tempor incididunt ut labore et dolore magna aliqua.</li>
    <li style="top:319px">Lorem ipsum dolor sit consectetur adipiscing elit, sed do eiusmod</li>
  </ul>
</section>

</body>
</html>
```